Business card for psychiatrist

Business card design project for a psychiatristWe would like to have the impression of 1. We (patient and the doctor) are working together.2. Light the way so that patients can see where they are going and what their goals are.3. One side of the business card will have the letter "TFP" which stands for Thornvale Family Psychiatry.4. The other side of the business card will have the address, phone number, name of the psychiatrist, website, etc.5. A logo could go into either side of the business card. Let's see what looks better.
Business card design project for a psychiatrist
We would like to have the impression of
1. We (patient and the doctor) are working together.
2. Light the way so that patients can see where they are going and what their goals are.
3. One side of the business card will have the letter "TFP" which stands for Thornvale Family Psychiatry.
4. The other side of the business card will have the address, phone number, name of the psychiatrist, website, etc.
5. A logo could go into either side of the business card. Let's see what looks better.
Colors
Designer to choose colors to be used in the design.
Look and feel
Each slider illustrates characteristics of the customer's brand and the style your logo design should communicate.

```html
<!DOCTYPE html>
<html lang="en">
<head>
<meta charset="utf-8">
<title>Thornvale Family Psychiatry — Business Card</title>
<link href="https://fonts.googleapis.com/css2?family=Cinzel:wght@500&family=Open+Sans:wght@400&display=swap" rel="stylesheet">
<style>
  :root {
    --stage-light: #5c5c5c;
    --stage-dark: #151515;
    --card: #ffffff;
    --accent: #f39420;
    --ink: #555555;
    --icon: #666666;
  }
  * { margin: 0; padding: 0; box-sizing: border-box; }
  html, body { width: 1200px; height: 999px; overflow: hidden; }
  body {
    position: relative;
    background: radial-gradient(ellipse 70% 75% at 50% 50%, var(--stage-light) 0%, #3a3a3a 55%, var(--stage-dark) 100%);
    font-family: "Open Sans", Arial, sans-serif;
  }
  .card {
    position: absolute;
    width: 829px;
    height: 474px;
    background: var(--card);
    border-radius: 32px;
    box-shadow: 0 4px 14px rgba(0,0,0,0.45);
    overflow: hidden;
  }
  .card--front { left: 130px; top: 25px; }
  .card--back { left: 251px; top: 514px; }

  .wordmark {
    position: absolute;
    font-family: "Open Sans", Arial, sans-serif;
    font-weight: 400;
    color: var(--accent);
    line-height: 1;
  }
  .wordmark__name, .wordmark__sub { display: block; white-space: nowrap; }

  .card--front .wordmark { left: 114px; top: 88px; }
  .card--front .wordmark__name { font-size: 42px; letter-spacing: 1px; }
  .card--front .wordmark__sub { font-size: 19px; margin-top: 8px; margin-left: 16px; letter-spacing: 1px; }

  .card--back .wordmark { left: 303px; top: 190px; }
  .card--back .wordmark__name { font-size: 56px; letter-spacing: 1px; }
  .card--back .wordmark__sub { font-size: 25px; margin-top: 10px; margin-left: 20px; letter-spacing: 1.5px; }

  .holder { position: absolute; left: 43px; top: 297px; display: flex; align-items: baseline; }
  .holder__name { font-family: "Cinzel", Georgia, serif; font-weight: 500; font-size: 39px; color: var(--accent); }
  .holder__role { font-size: 18px; color: var(--ink); margin-left: 22px; }

  .divider { position: absolute; left: 0; top: 347px; width: 100%; height: 3px; background: var(--accent); }

  .contacts { position: absolute; left: 42px; top: 359px; list-style: none; }
  .contacts li { display: flex; align-items: center; height: 26px; font-size: 18px; color: var(--ink); }
  .contacts svg { width: 16px; height: 16px; margin-right: 17px; fill: none; stroke: var(--icon); stroke-width: 1.8; }
  .address { position: absolute; left: 581px; top: 384px; font-size: 18px; color: var(--ink); line-height: 24px; }
</style>
</head>
<body>
  <section class="card card--front">
    <div class="wordmark">
      <span class="wordmark__name">Thornvale</span>
      <span class="wordmark__sub">Family Psychiatry</span>
    </div>
    <div class="holder">
      <span class="holder__name">Name Title</span>
      <span class="holder__role">designation</span>
    </div>
    <div class="divider"></div>
    <ul class="contacts">
      <li><svg viewBox="0 0 16 16"><path d="M3 2l3 0 1 3-2 1.5a8 8 0 0 0 4.5 4.5L11 9l3 1v3a1 1 0 0 1-1 1A12 12 0 0 1 2 3a1 1 0 0 1 1-1z"/></svg>000-000-0000</li>
      <li><svg viewBox="0 0 16 16"><path d="M2 7l6-5 6 5v7H2z"/><path d="M2 7l6 4 6-4"/></svg>abcde@abcdefg.com</li>
      <li><svg viewBox="0 0 16 16"><circle cx="8" cy="8" r="6"/><path d="M2 8h12M8 2c-3 3.5-3 8.5 0 12M8 2c3 3.5 3 8.5 0 12"/></svg>www.abcdefg.com</li>
    </ul>
    <p class="address">suit # 00, Lorem ipsum<br>Lorem Lorem ipsum</p>
  </section>

  <section class="card card--back">
    <div class="wordmark">
      <span class="wordmark__name">Thornvale</span>
      <span class="wordmark__sub">Family Psychiatry</span>
    </div>
  </section>
</body>
</html>
```